Property Management Card

We are owners of a property management and real estate company. We manage many residential buildings in our area and would like to send cards to neighboring propertiies. I have attached a card that was designed for us that we do not like but has pertinent information and branding, font style, etc. We want something that will grab people's attention as they sift through their junk mail.

Here is information we would like included:

We manage the property at________(we will fill in the blank)
We can manage yours, too!

We offer
24 hour emergency line
online rent payment for tenants
the best trades people in the South Bay
5 full time employees who speak English and Spanish
Business for over 36 years

Call Mark Holloway for a free quote at 310-847-2093

Target Market(s)

Industry/Entity Type

Real Estate

Requirements
Must have
• We manage the property at________(we will fill in the blank)
• We can manage yours, too!
• We offer
• 24 hour emergency line
• online rent payment for tenants
• the best trades people in the South Bay
• 5 full time employees who speak English and Spanish
• Business for over 36 years
• Call Mark Holloway for a free quote at 310-847-2093
• Email address mark@brindlecrestmgmt.com
• website brindlecrestharborproperties.com
• Broker BRE 04817352
• office address is
• 18 Tessaly Court, Suite 4
• Palos Verdes Estates, CA 90318
• two sided
• space for a mailing address and postage
• our branding/logo
• font to coordinate with branding
• postcard to be 279mm x 152 mm (full bleed size is 282 mm x 155mm, 3335x1835 pixels)
• vertical or horizontal orientation up to designers creativity. Again, what ever will draw attention
• (our branding colors are a dark gray/charcoal, white and dark sand. see postcard and logo for example of colors)
Nice to have
• images to draw attention to owners who would like a property manager
• we would like to have our photo. if this compromises design then we are happy to delete it. the photo can be on either side

```html
<!DOCTYPE html>
<html lang="en">
<head>
<meta charset="utf-8">
<title>Holloway Associates – Property Management Postcard</title>
<link rel="stylesheet" href="https://fonts.googleapis.com/css2?family=Open+Sans:wght@400;600;700;800&family=PT+Sans:wght@700&display=swap">
<style>
  :root {
    --stage: #b8b9bb;
    --charcoal: #3a3a3c;
    --sand: #a89d8d;
    --sand-dark: #8a7f71;
    --white: #ffffff;
    --red: #c1202d;
    --ink: #333335;
    --photo-light: #eceae6;
    --photo-mid: #d6d2cb;
  }
  * { box-sizing: border-box; margin: 0; padding: 0; }
  html, body { width: 947px; height: 1200px; overflow: hidden; }
  body { background: var(--stage); font-family: "Open Sans", sans-serif; position: relative; }

  .side-label {
    position: absolute; left: 0; width: 947px; text-align: center;
    font-family: "PT Sans", sans-serif; font-weight: 700; font-size: 72px;
    color: var(--charcoal); line-height: 1;
  }
  .side-label--front { top: 16px; }
  .side-label--back { top: 596px; }

  .card { position: absolute; left: 31px; width: 885px; height: 482px; overflow: hidden;
          box-shadow: 2px 3px 6px rgba(0,0,0,.3); }
  .card--front { top: 94px; background: var(--white); }
  .card--back { top: 682px; height: 483px; background: var(--white); }

  /* FRONT */
  .front__scene { position: absolute; left: 0; top: 180px; width: 885px; height: 302px;
                  background: linear-gradient(100deg, var(--photo-light) 0%, #f5f4f1 45%, var(--photo-mid) 100%); }
  .front__band { position: absolute; left: 0; top: 0; width: 885px; height: 180px; background: var(--charcoal); }
  .brand { position: absolute; color: var(--white); font-weight: 400; text-transform: uppercase; line-height: 1; }
  .brand--front { left: 18px; top: 40px; font-size: 34px; letter-spacing: .5px; }
  .brand span { display: block; margin-bottom: 4px; }

  .headline { position: absolute; left: 283px; top: 22px; width: 575px; height: 208px;
              background: var(--charcoal); border-radius: 0 0 36px 36px; padding: 6px 8px 8px; }
  .headline__top { height: 70px; background: var(--sand); color: var(--white);
                   font-weight: 700; font-size: 37px; line-height: 70px; text-align: center; }
  .headline__blank { height: 58px; background: var(--white); position: relative; }
  .headline__blank::after { content: ""; position: absolute; left: 16px; right: 16px; top: 44px;
                            height: 4px; background: var(--charcoal); }
  .headline__bottom { height: 66px; background: var(--sand); color: var(--white); border-radius: 0 0 30px 30px;
                      font-weight: 700; font-size: 37px; line-height: 62px; text-align: center; }

  .burst { position: absolute; left: 15px; top: 202px; width: 256px; height: 256px; }
  .burst svg { position: absolute; inset: 0; }
  .burst__text { position: absolute; left: 0; top: 0; width: 256px; height: 256px;
                 display: flex; flex-direction: column; align-items: center; justify-content: center;
                 transform: rotate(-30deg); color: var(--white); font-weight: 800; line-height: .9; }
  .burst__big { font-size: 50px; }
  .burst__small { font-size: 33px; }

  .offer { position: absolute; left: 300px; top: 244px; width: 540px; text-align: center; color: var(--ink); }
  .offer__title { font-family: "PT Sans", sans-serif; font-weight: 700; font-size: 27px; margin-bottom: 6px; }
  .offer__list { list-style: none; font-size: 19px; line-height: 29.5px; }

  .front__web { position: absolute; left: 286px; top: 420px; width: 599px; height: 62px;
                background: var(--sand); border-radius: 32px 0 0 0; color: var(--white);
                font-weight: 700; font-size: 21px; letter-spacing: 5.4px; line-height: 62px; padding-left: 56px; }

  /* BACK */
  .back__panel { position: absolute; left: 0; top: 0; width: 442px; height: 483px;
                 background: linear-gradient(160deg, #b0a594 0%, var(--sand-dark) 55%, #9a8f80 100%); }
  .mail-area { position: absolute; left: 442px; top: 0; width: 443px; height: 483px; background: var(--white); }
  .quote-tab { position: absolute; left: 0; top: 22px; width: 253px; height: 57px; background: var(--charcoal);
               color: var(--white); font-family: "PT Sans", sans-serif; font-weight: 700; font-size: 19px;
               line-height: 21px; text-align: center; padding-top: 7px; }
  .portrait { position: absolute; left: 253px; top: 22px; width: 172px; height: 216px;
              background: var(--charcoal); border-radius: 0 0 34px 34px; padding: 6px; }
  .portrait__fill { width: 100%; height: 100%; border-radius: 0 0 28px 28px;
                    background: linear-gradient(180deg, #a59a8d 0%, #5a534c 60%, #2b2a2a 100%); }
  .agent { position: absolute; right: 644px; top: 110px; width: 240px; text-align: right; line-height: 1.25; }
  .agent__name { font-family: "PT Sans", sans-serif; font-weight: 700; font-size: 24px; color: var(--charcoal); line-height: 1.1; }
  .agent__line { color: var(--white); font-size: 17px; }
  .agent__line--mail { font-size: 15px; }
  .agent__line--lic { font-size: 13px; font-weight: 600; }
  .brand-tab { position: absolute; left: 0; top: 224px; width: 233px; height: 108px; background: var(--charcoal);
               border-radius: 0 32px 32px 0; }
  .brand--back { left: 24px; top: 24px; font-size: 29px; }
  .contact { position: absolute; left: 24px; top: 338px; color: var(--white); font-size: 15.5px; line-height: 16px; font-weight: 600; }
  .contact__gap { margin-top: 10px; }
  .back__web { position: absolute; left: 0; top: 422px; width: 345px; height: 61px; background: var(--charcoal);
               border-radius: 0 32px 0 0; color: var(--white); font-size: 17px; line-height: 61px; padding-left: 24px; }
</style>
</head>
<body>
  <div class="side-label side-label--front">FRONT</div>

  <section class="card card--front">
    <div class="front__scene" role="img" aria-label="Bright balcony with iron railing overlooking the ocean"></div>
    <div class="front__band"></div>
    <div class="brand brand--front"><span>Holloway</span><span>Associates</span></div>

    <div class="headline">
      <div class="headline__top">We manage the property at</div>
      <div class="headline__blank"></div>
      <div class="headline__bottom">We can manage yours, too!</div>
    </div>

    <div class="burst">
      <svg viewBox="-130 -130 260 260" aria-hidden="true">
        <g fill="var(--red)">
          <rect x="-90.5" y="-90.5" width="181" height="181"/>
          <rect x="-90.5" y="-90.5" width="181" height="181" transform="rotate(10)"/>
          <rect x="-90.5" y="-90.5" width="181" height="181" transform="rotate(20)"/>
          <rect x="-90.5" y="-90.5" width="181" height="181" transform="rotate(30)"/>
          <rect x="-90.5" y="-90.5" width="181" height="181" transform="rotate(40)"/>
          <rect x="-90.5" y="-90.5" width="181" height="181" transform="rotate(50)"/>
          <rect x="-90.5" y="-90.5" width="181" height="181" transform="rotate(60)"/>
          <rect x="-90.5" y="-90.5" width="181" height="181" transform="rotate(70)"/>
          <rect x="-90.5" y="-90.5" width="181" height="181" transform="rotate(80)"/>
          <circle r="104"/>
        </g>
      </svg>
      <div class="burst__text">
        <span class="burst__big">24 hour</span>
        <span class="burst__small">emergency</span>
        <span class="burst__small">line</span>
      </div>
    </div>

    <div class="offer">
      <h2 class="offer__title">HERE IS WHAT WE HAVE TO OFFER:</h2>
      <ul class="offer__list">
        <li>Tenants can pay on-line</li>
        <li>Some the best trades people in the South Bay</li>
        <li>5 full time employees who speak English and Spanish</li>
        <li>Business for over 36 years</li>
      </ul>
    </div>

    <div class="front__web">brindlecrestharborproperties.com</div>
  </section>

  <div class="side-label side-label--back">BACK</div>

  <section class="card card--back">
    <div class="back__panel" role="img" aria-label="Soft sand-toned view of a terrace with railing and patio chair"></div>
    <div class="mail-area"></div>
    <div class="quote-tab">CALL MARK HOLLOWAY FOR<br>A FREE QUOTE</div>
    <div class="portrait"><div class="portrait__fill" role="img" aria-label="Portrait photo of the broker and his partner"></div></div>

    <div class="agent">
      <div class="agent__name">MARK HOLLOWAY</div>
      <div class="agent__line">310.847.2093</div>
      <div class="agent__line agent__line--mail">mark@brindlecrestmgmt.com</div>
      <div class="agent__line agent__line--lic">BROKER BRE 04817352</div>
    </div>

    <div class="brand-tab">
      <div class="brand brand--back"><span>Holloway</span><span>Associates</span></div>
    </div>

    <div class="contact">
      <div>Office # 310-642-7185</div>
      <div>Cell # 310-847-2093</div>
      <div class="contact__gap">18 Tessaly Court, Suite 4,</div>
      <div>Palos Verdes Estates, CA 90318</div>
    </div>

    <div class="back__web">brindlecrestharborproperties.com</div>
  </section>
</body>
</html>
```